Business Card Design Project

Bold, modern, clean business card design needed. Prefer double sided with art logo on the back. Front of card with company name logo, no art.

Target Market(s)

Our consulting company supports local, state and federal law enforcement officers. Therefore the design should be clean and direct with no flash or arrogance to it.

Industry/Entity Type

Business

```html
<!DOCTYPE html>
<html lang="en">
<head>
<meta charset="utf-8">
<title>Halden Consulting – Business Card</title>
<link href="https://fonts.googleapis.com/css2?family=Michroma&family=Jura:wght@500&display=swap" rel="stylesheet">
<style>
  :root {
    --paper: #ffffff;
    --ink: #1c1c1c;
    --ink-soft: #3a3a3a;
    --lime: #8cd212;
    --lime-deep: #3f7a08;
    --lime-bright: #9ef01a;
    --night: #0f1212;
    --night-glow: #2a2f2f;
    --silver: #c9cccc;
    --silver-light: #eceeee;
  }
  * { margin: 0; padding: 0; box-sizing: border-box; }
  html, body { width: 1200px; height: 347px; overflow: hidden; background: var(--paper); }
  .canvas { position: relative; width: 1200px; height: 347px; display: flex; }

  /* Front side */
  .card-front { position: relative; width: 621px; height: 347px; background: var(--paper); }
  .front-brand {
    position: absolute; left: 88px; top: 150px; width: 180px;
    display: flex; flex-direction: column; align-items: center; gap: 12px;
  }
  .brand-dot { width: 34px; height: 34px; border-radius: 50%; background: var(--lime); }
  .brand-name {
    font-family: "Michroma", sans-serif; color: var(--ink);
    font-size: 15px; line-height: 1.35; text-align: center; letter-spacing: 1px;
  }
  .holder-name {
    position: absolute; right: 92px; top: 60px;
    font-family: "Jura", sans-serif; font-weight: 500;
    font-size: 19px; letter-spacing: 2.5px; color: var(--ink);
  }
  .contact-list { position: absolute; right: 92px; top: 108px; list-style: none; }
  .contact-item {
    display: flex; align-items: center; justify-content: flex-end; gap: 10px;
    height: 33px;
    font-family: "Michroma", sans-serif; font-size: 10px; letter-spacing: 1.2px;
    text-transform: uppercase; color: var(--ink-soft);
  }
  .contact-icon {
    width: 21px; height: 21px; border-radius: 50%; background: var(--lime);
    display: flex; align-items: center; justify-content: center; flex: none;
  }
  .contact-icon svg { width: 12px; height: 12px; fill: var(--paper); }

  /* Back side */
  .card-back {
    position: relative; width: 579px; height: 347px; overflow: hidden;
    background: radial-gradient(ellipse at 50% 45%, var(--night-glow) 0%, var(--night) 70%);
  }
  .back-brand {
    position: absolute; left: 0; right: 0; top: 92px;
    display: flex; flex-direction: column; align-items: center; gap: 22px;
  }
  .back-brand .brand-dot { width: 70px; height: 70px; }
  .back-brand .brand-name { color: var(--silver-light); font-size: 38px; letter-spacing: 3px; line-height: 1.2; }
  .back-rule {
    position: absolute; left: 0; right: 0; top: 290px; height: 7px;
    background: linear-gradient(to bottom, var(--silver-light), var(--silver) 60%, #8d9191);
  }
  .back-band {
    position: absolute; left: 0; right: 0; top: 297px; bottom: 0;
    background: radial-gradient(ellipse at 50% 40%, var(--lime-bright) 0%, var(--lime) 40%, var(--lime-deep) 100%);
  }
</style>
</head>
<body>
<main class="canvas">
  <section class="card-front">
    <div class="front-brand">
      <span class="brand-dot"></span>
      <p class="brand-name">HALDEN CONSULTING</p>
    </div>
    <h1 class="holder-name">Mark Ellison</h1>
    <ul class="contact-list">
      <li class="contact-item">555 014 728
        <span class="contact-icon"><svg viewBox="0 0 24 24"><path d="M6.6 10.8a15 15 0 0 0 6.6 6.6l2.2-2.2c.3-.3.7-.4 1-.2 1.1.4 2.3.6 3.6.6.6 0 1 .4 1 1V20c0 .6-.4 1-1 1A17 17 0 0 1 3 4c0-.6.4-1 1-1h3.5c.6 0 1 .4 1 1 0 1.3.2 2.5.6 3.6.1.3 0 .7-.2 1z"/></svg></span>
      </li>
      <li class="contact-item">Your address no.65
        <span class="contact-icon"><svg viewBox="0 0 24 24"><path d="M12 3 2 12h3v8h5v-5h4v5h5v-8h3z"/></svg></span>
      </li>
      <li class="contact-item">Social/name
        <span class="contact-icon"></span>
      </li>
      <li class="contact-item">Network/name
        <span class="contact-icon"></span>
      </li>
      <li class="contact-item">your@email.com
        <span class="contact-icon"><svg viewBox="0 0 24 24"><path d="M3 6h18v12H3z M3 6l9 7 9-7" fill="none" stroke="#fff" stroke-width="2"/></svg></span>
      </li>
      <li class="contact-item">www.yourwebsite.com
        <span class="contact-icon"><svg viewBox="0 0 24 24"><path d="M6 3v16l4-4 3 6 3-1.5-3-6h5z"/></svg></span>
      </li>
    </ul>
  </section>

  <section class="card-back">
    <div class="back-brand">
      <span class="brand-dot"></span>
      <p class="brand-name">HALDEN CONSULTING</p>
    </div>
    <div class="back-rule"></div>
    <div class="back-band"></div>
  </section>
</main>
</body>
</html>
```